Delmer's Pressure Washing Services

Starting a pressure washing business on my own in Central Valley California, not too much experience so affordable, I do houses, fences, driveways, cars, trailers, RVs. Planning to make this full-time hoping clientele picks up after having a nice business card. Design doesn't have to be flashy, more to the point, I like simplistic/personable. I do not want something exhausting to look at or with too much going on.

Target Market(s)

Residential, Commercial

Industry/Entity Type

Pressure Washing

Contact Information for Business Card

avalible Services

Font styles to use
Sans Serif

Colors
0054AA
0677BA
7BADD7
CADEEF
E8F1F8
0094D4
00A9DD
6FCCEA
C7EBF8
E9F6FB
00AB8E
00BBA5
67D7C9
C6EFE9
E9F9F6

```html
<!DOCTYPE html>
<html lang="en">
<head>
<meta charset="utf-8">
<title>Delmer's Pressure Washing Services – Business Card</title>
<link href="https://fonts.googleapis.com/css2?family=Audiowide&family=Montserrat:wght@400;600&display=swap" rel="stylesheet">
<style>
  :root {
    --page-bg: #e6e6e6;
    --navy-deep: #06123a;
    --navy: #0a2460;
    --blue-brand: #0054aa;
    --blue-mid: #0677ba;
    --blue-light: #7badd7;
    --blue-pale: #cadeef;
    --blue-mist: #e8f1f8;
    --teal-glow: #0094d4;
    --ink: #111827;
    --white: #ffffff;
    --paper: #f1f2f3;
  }
  * { box-sizing: border-box; margin: 0; padding: 0; }
  html, body { width: 685px; height: 1200px; overflow: hidden; background: var(--page-bg); }
  .canvas { position: relative; width: 685px; height: 1200px; }

  .card {
    position: absolute; left: 102px; width: 480px; height: 274px;
    overflow: hidden; box-shadow: 0 3px 6px rgba(0,0,0,.25);
  }
  .card--front { top: 300px;
    background:
      radial-gradient(circle at 80% 25%, rgba(0,148,212,.45), transparent 35%),
      radial-gradient(circle at 25% 75%, rgba(6,119,186,.35), transparent 30%),
      radial-gradient(circle at 60% 60%, rgba(6,119,186,.25), transparent 40%),
      linear-gradient(160deg, var(--navy-deep) 0%, #0b2a66 55%, #0c3f80 100%);
  }
  .card--back { top: 630px;
    background: linear-gradient(135deg, #dff1fb 0%, var(--white) 40%, var(--blue-mist) 100%);
  }

  .brand-name { font-family: "Audiowide", sans-serif; font-weight: 400; }

  .front-brand { position: absolute; top: 72px; left: 0; width: 100%; text-align: center; color: var(--white); }
  .front-brand__main { font-size: 38px; line-height: 1.1; letter-spacing: 1px; }
  .front-brand__sub { font-size: 19px; line-height: 1.3; }
  .front-band { position: absolute; left: 0; bottom: 0; width: 480px; height: 60px; }
  .front-url {
    position: absolute; left: 0; width: 100%; top: 232px; text-align: center;
    font-family: "Montserrat", sans-serif; font-weight: 600; font-size: 13px;
    letter-spacing: 4px; color: var(--ink);
  }
  .front-url .accent { color: var(--blue-brand); }

  .back-panel { position: absolute; inset: 0; }
  .back-brand { position: absolute; left: 28px; top: 28px; color: var(--blue-brand); }
  .back-brand__main { font-size: 22px; line-height: 1.1; }
  .back-brand__sub { font-size: 11px; line-height: 1.4; }

  .person { position: absolute; left: 27px; top: 100px; font-family: "Montserrat", sans-serif; }
  .person__name { font-size: 17px; color: var(--ink); font-weight: 400; letter-spacing: .3px; }
  .person__name strong { font-weight: 600; }
  .person__role { font-size: 11px; color: var(--blue-mid); }

  .contacts { position: absolute; left: 0; top: 151px; list-style: none; font-family: "Montserrat", sans-serif; }
  .contacts li { display: flex; align-items: center; height: 17px; margin-bottom: 9.5px; font-size: 14px; color: var(--ink); }
  .contacts .icon-tab {
    width: 44px; height: 17px; background: var(--blue-brand); margin-right: 10px;
    display: flex; align-items: center; justify-content: flex-end; padding-right: 6px;
  }

  .services { position: absolute; left: 306px; top: 70px; color: var(--white); }
  .services__title { font-family: "Audiowide", sans-serif; font-size: 14px; margin-left: 9px; }
  .services__list { list-style: none; margin-top: 6px; margin-left: 12px; font-family: "Audiowide", sans-serif; font-size: 11px; }
  .services__list li { height: 18px; display: flex; align-items: center; }
  .services__list li::before {
    content: ""; width: 7px; height: 2px; background: var(--white); margin-right: 12px; border-radius: 1px;
  }
  .services__bracket { position: absolute; left: 0; top: 10px; }
</style>
</head>
<body>
<main class="canvas">

  <section class="card card--front" aria-label="Business card front">
    <div class="front-brand brand-name">
      <div class="front-brand__main">Delmer's</div>
      <div class="front-brand__sub">Pressure Washing</div>
    </div>
    <svg class="front-band" viewBox="0 0 480 60" aria-hidden="true">
      <path d="M0,22 Q240,-14 480,22 L480,60 L0,60 Z" fill="var(--paper)"/>
    </svg>
    <div class="front-url">www.<span class="accent">delmerswash</span>.com</div>
  </section>

  <section class="card card--back" aria-label="Business card back">
    <svg class="back-panel" viewBox="0 0 480 274" aria-hidden="true">
      <path d="M0,0 L140,0 L0,60 Z" fill="var(--blue-pale)" opacity=".5"/>
      <path d="M0,245 Q40,270 70,274 L0,274 Z" fill="var(--blue-light)" opacity=".6"/>
    </svg>
    <svg class="back-panel" viewBox="0 0 480 274" role="img" aria-label="Dark blue panel with fine line mesh pattern">
      <defs>
        <linearGradient id="panelFill" x1="0" y1="0" x2="1" y2="1">
          <stop offset="0" stop-color="#081c52"/>
          <stop offset="1" stop-color="#0b3a96"/>
        </linearGradient>
      </defs>
      <path d="M286,0 C222,55 210,205 291,274 L480,274 L480,0 Z" fill="url(#panelFill)"/>
    </svg>

    <div class="back-brand brand-name">
      <div class="back-brand__main">Delmer's</div>
      <div class="back-brand__sub">Pressure Washing</div>
    </div>

    <div class="person">
      <div class="person__name">DELMER <strong>RUIZ</strong></div>
      <div class="person__role">Owner</div>
    </div>

    <ul class="contacts">
      <li><span class="icon-tab"><svg width="11" height="11" viewBox="0 0 24 24"><path d="M6.6 10.8a15 15 0 0 0 6.6 6.6l2.2-2.2c.3-.3.7-.4 1-.2 1.1.4 2.3.6 3.6.6.6 0 1 .4 1 1V20c0 .6-.4 1-1 1A17 17 0 0 1 3 4c0-.6.4-1 1-1h3.5c.6 0 1 .4 1 1 0 1.3.2 2.5.6 3.6.1.3 0 .7-.2 1z" fill="#fff"/></svg></span>5595550147</li>
      <li><span class="icon-tab"><svg width="11" height="9" viewBox="0 0 22 16"><rect x="1" y="1" width="20" height="14" fill="none" stroke="#fff" stroke-width="2"/><path d="M1 1l10 8 10-8" fill="none" stroke="#fff" stroke-width="2"/></svg></span>info@delmerswash.com</li>
      <li><span class="icon-tab"><svg width="11" height="11" viewBox="0 0 24 24" fill="none" stroke="#fff" stroke-width="2"><circle cx="12" cy="12" r="10"/><path d="M2 12h20M12 2c3 3 3 17 0 20M12 2c-3 3-3 17 0 20"/></svg></span>www.delmerswash.com</li>
    </ul>

    <div class="services">
      <svg class="services__bracket" width="140" height="140" viewBox="0 0 140 140" aria-hidden="true">
        <path d="M6,2 Q1,2 1,8 L1,128 Q1,134 8,134 L108,134" fill="none" stroke="#fff" stroke-width="1.6"/>
        <rect x="104" y="131" width="14" height="6" rx="3" fill="#fff"/>
      </svg>
      <div class="services__title">Our Services</div>
      <ul class="services__list">
        <li>Houses</li>
        <li>Fences</li>
        <li>Driveways</li>
        <li>Cars</li>
        <li>Trailers</li>
        <li>RVs</li>
      </ul>
    </div>
  </section>

</main>
</body>
</html>
```